Buch-/E-Book-Cover Existenzgründer und Gründungsinteressierte
Zielgruppe
Es geht um eine Buchcover mit dem Titel 'Wolkenhafen erkunden'; Zielgruppe sind Existenzgründer und Gründungsinteressierte
Aufgabenstellung
Das Buchcover sollte modern und frisch gestaltet werden, eine grobe Skizze ist beigefügt, unten rechts soll das Verlagslogo (klein) platziert werden
Haupttext „Wolkenhafen erkunden“ soll auffallend, vielleicht als Wortmarke, gestaltet werden – er sollte einen Wiedererkennungswert haben
Auf der Frontseite des Covers sollten auch die Schlüsselwörter zu den Hauptkapiteln integriert werden (siehe Idee Skizze), damit der Leser auf den 1. Blick einen Eindruck über die Inhalte des Ratgebers gewinnt
Format: Das Taschenbuch soll im Hochformat (13,97 cm x 21,59 cm, Bindung links, Veltrano Quill Print Service) erscheinen und das Buch hat ca. 190 Seiten. Das Cover soll ein Softcover (235g Chromokarton), 4/4 farbig sein.

```html
<!DOCTYPE html>
<html lang="de">
<head>
<meta charset="utf-8">
<title>Wolkenhafen erkunden – Buchcover</title>
<link href="https://fonts.googleapis.com/css2?family=Russo+One&family=Roboto+Condensed:wght@400;700&display=swap" rel="stylesheet">
<style>
  :root {
    --canvas: #c4c5c7;
    --paper: #f4f4f6;
    --navy: #2d2a7c;
    --band-top: #2c2986;
    --band-bottom: #5a2f98;
    --accent: #f6a623;
    --white: #ffffff;
  }
  html, body {
    margin: 0;
    padding: 0;
    width: 803px;
    height: 1200px;
    overflow: hidden;
    background: var(--canvas);
  }
  .stage {
    position: relative;
    width: 803px;
    height: 1200px;
  }
  .cover-spread {
    position: absolute;
    left: 21px;
    top: 327px;
    width: 850px;
    height: 611px;
    transform: scale(0.894);
    transform-origin: 0 0;
    background: var(--paper);
    box-shadow: 6px 8px 14px rgba(0,0,0,0.35);
    font-family: "Roboto Condensed", "Arial Narrow", sans-serif;
    overflow: hidden;
  }
  .band {
    position: absolute;
    left: 0;
    top: 213px;
    width: 850px;
    height: 253px;
    background: linear-gradient(180deg, var(--band-top), var(--band-bottom));
  }
  .spine {
    position: absolute;
    left: 396px;
    top: 0;
    width: 57px;
    height: 611px;
    background: linear-gradient(180deg, var(--band-top), var(--band-bottom));
  }
  .spine-title {
    position: absolute;
    left: 0;
    top: 192px;
    width: 57px;
    margin: 0;
    writing-mode: vertical-rl;
    line-height: 57px;
    white-space: nowrap;
    font-family: "Russo One", sans-serif;
    font-weight: 400;
    font-size: 27px;
    color: var(--accent);
  }
  .subtitle {
    position: absolute;
    margin: 0;
    font-weight: 700;
    font-size: 19px;
    line-height: 26px;
    color: var(--navy);
  }
  .back .subtitle { left: 38px; top: 150px; }
  .blurb {
    position: absolute;
    left: 38px;
    top: 226px;
    width: 320px;
    color: var(--white);
    font-size: 11.6px;
    line-height: 18px;
  }
  .blurb p { margin: 0 0 18px; }
  .title {
    position: absolute;
    left: 475px;
    top: 32px;
    margin: 0;
    font-family: "Russo One", sans-serif;
    font-weight: 400;
    font-size: 36px;
    line-height: 48px;
    color: var(--accent);
  }
  .front .subtitle { left: 478px; top: 138px; }
  .topics {
    position: absolute;
    left: 482px;
    top: 231px;
    color: var(--white);
  }
  .topics h3 {
    margin: 0 0 5px;
    font-size: 14.5px;
    font-weight: 700;
  }
  .topics ul {
    list-style: none;
    margin: 0;
    padding: 0;
    font-size: 14.5px;
    line-height: 21.5px;
  }
  .topics li {
    position: relative;
    padding-left: 15px;
  }
  .topics li::before {
    content: "";
    position: absolute;
    left: 0;
    top: 7px;
    width: 8px;
    height: 8px;
    border-radius: 50%;
    background: radial-gradient(circle, var(--white) 0 2px, transparent 2.5px);
    border: 1px solid var(--white);
    box-sizing: border-box;
  }
  .topics li.cont { padding-left: 17px; }
  .topics li.cont::before { display: none; }
  .illustration {
    position: absolute;
    left: 680px;
    top: 176px;
    width: 166px;
    height: 276px;
    border-radius: 10px;
    background:
      radial-gradient(ellipse at 60% 45%, #f7a22a 0%, #e85a2a 38%, rgba(90,47,152,0) 70%),
      linear-gradient(180deg, rgba(230,60,50,0.5), rgba(60,40,130,0.4));
  }
  .author {
    position: absolute;
    left: 571px;
    top: 562px;
    margin: 0;
    font-weight: 700;
    font-size: 19px;
    color: var(--navy);
  }
  .publisher {
    position: absolute;
    right: 22px;
    top: 536px;
    width: 60px;
    text-align: right;
    font-weight: 700;
    font-size: 12px;
    line-height: 14px;
    color: var(--navy);
  }
</style>
</head>
<body>
<main class="stage">
  <div class="cover-spread">
    <div class="band"></div>

    <section class="back">
      <h2 class="subtitle">Existenzgründung<br>für Kleinunternehmen</h2>
      <div class="blurb">
        <p>Lorem ipsum dolor sit amet, consectetur adipiscing elit, sed do eiusmod tempor incididunt ut labore et dolore magna aliqua. Sed lectus vestibulum mattis ullamcorper velit sed ullamcorper morbi tincidunt. Ultricies mi eget mauris pharetra et. Lectus quam id leo in vitae turpis massa sed. Laoreet suspendisse interdum consectetur libero id faucibus. Morbi tristique senectus et netus et malesuada fames. Donec adipiscing tristique risus nec feugiat in fermentum posuere urna. Diam volutpat commodo sed egestas egestas fringilla phasellus faucibus.</p>
        <p>Lorem ipsum dolor sit amet, consectetur adipiscing elit, sed do eiusmod tempor incididunt ut labore et dolore magna aliqua. Egestas dui id ornare arcu odio ut sem nulla. Urna nunc id cursus metus.</p>
      </div>
    </section>

    <section class="spine">
      <p class="spine-title">Wolkenhafen erkunden</p>
    </section>

    <section class="front">
      <h1 class="title">Wolkenhafen<br>erkunden</h1>
      <h2 class="subtitle">Existenzgründung<br>für Kleinunternehmen</h2>
      <div class="topics">
        <h3>Alles über:</h3>
        <ul>
          <li>Behördengänge</li>
          <li>Rechtsform</li>
          <li>(digitale) Büroorganisation</li>
          <li>Buchhaltung und steuern</li>
          <li>Finanzierung und Fördelmittel</li>
          <li>Businessplan</li>
          <li>Versicherungen</li>
          <li>Bonus: Online-</li>
          <li class="cont">Trainings und Vorlagen</li>
        </ul>
      </div>
      <div class="illustration" role="img" aria-label="Illustration: startende Rakete mit Zielscheibe und kleinem Balkendiagramm"></div>
      <p class="author">von Matthias Kernbach</p>
      <div class="publisher">Zahlenfroh Verlag</div>
    </section>
  </div>
</main>
</body>
</html>
```